Tradeo Cup Championship Webdesign project

We need a webdesign for the project called TradeoCup. TradeoCup™ is an international Forex trading competition to see who can make the most profit in two weeks with all players getting an equal starting sum. Participation is free with no strings attached and the prize money is real, with a total prize pool of $50,000! At the moment TradeoCup vol. 2 is about to get launched and we would like to have a new design. On the new website traders should be able to create their own competitions, as well as to invite each other for the cometition.
Updates

Project Deadline Extended

Project Deadline Extended

Requirements
Must have
• http://www.tradeocup-example.com/ please refer to this website for the further details.

The website should also include the competition section where traders can invite each other for the competition. It should work similarly to poker competitions.

```html
<!DOCTYPE html>
<html lang="en">
<head>
<meta charset="utf-8">
<title>TradeoCup – International Trading Championship</title>
<link rel="stylesheet" href="https://fonts.googleapis.com/css2?family=Arimo:wght@400;700&display=swap">
<style>
:root{
  --navy:#0b2a4a;
  --blue-deep:#0e3a66;
  --blue:#1c5d97;
  --blue-light:#5c9fd0;
  --sky:#7fb7e0;
  --grey-bg:#e4e4e4;
  --grey-line:#c9c9c9;
  --grey-text:#555;
  --ink:#222;
  --white:#fff;
  --red:#e0262b;
}
*{box-sizing:border-box;margin:0;padding:0}
html,body{width:986px;height:1200px;overflow:hidden;background:var(--white)}
body{position:relative;font-family:"Arimo",Arial,sans-serif;color:var(--ink)}
.abs{position:absolute}

/* header */
.site-header{left:26px;top:8px;width:944px;height:114px;border-radius:0 0 16px 16px;
  background:linear-gradient(#f4f4f4,#bdbdbd);border:1px solid var(--grey-line)}
.brand-band{left:6px;top:12px;width:700px;height:82px;border-radius:10px 0 0 10px;
  background:linear-gradient(90deg,#7a8ea4 0%,var(--blue) 20%,var(--navy) 60%,var(--blue-deep) 100%)}
.brand{left:20px;top:20px;display:flex;align-items:center;gap:10px;color:var(--white);font-size:22px;font-weight:400}
.brand-dot{width:34px;height:34px;border-radius:50%;background:#c9c3b0}
.lang{left:510px;top:18px;display:flex;gap:8px;align-items:center}
.lang-flag{width:30px;height:20px;background:linear-gradient(#1f3f8a 0 40%,#fff 40% 60%,#c8202f 60%)}
.lang-select{width:160px;height:20px;background:var(--white);border:1px solid #999;font-size:11px;padding:2px 6px;position:relative}
.lang-select::after{content:"";position:absolute;right:4px;top:6px;border:5px solid transparent;border-top-color:#777}
.countdown-box{left:690px;top:18px;width:250px;height:72px;border-radius:6px;background:linear-gradient(#fafafa,#e1e1e1);border:1px solid var(--grey-line)}
.countdown{left:10px;top:8px;width:120px;text-align:center}
.countdown h3{font-size:11px;font-weight:700}
.countdown .timer{font-size:14px;color:#aaa;margin-top:6px;letter-spacing:1px}
.countdown .timer small{font-size:9px}
.participants{left:138px;top:8px;border-left:1px solid var(--grey-line);padding-left:10px;height:38px;display:flex;gap:14px}
.participants h3{font-size:8px;line-height:9px;font-weight:700}
.participants b{font-size:18px;color:var(--red);font-weight:400}
.box-links{left:0;top:55px;width:250px;font-size:9px;color:#999}
.box-links span{position:absolute}

/* nav */
.main-nav{left:26px;top:137px;width:944px;height:33px;background:var(--grey-bg);border-radius:3px;display:flex;justify-content:space-between;align-items:center;padding:0 6px}
.main-nav a{font-size:16px;font-weight:700;color:var(--grey-text);text-decoration:none}

/* hero */
.hero{left:26px;top:183px;width:663px;height:253px;border-radius:14px;overflow:hidden;background:linear-gradient(90deg,#0a1e38 0%,var(--blue-deep) 35%,#06182e 100%)}
.hero-art{left:0;top:0;width:360px;height:253px;background:radial-gradient(circle at 45% 55%,#4a86c0 0%,#174a7d 40%,transparent 75%)}
.hero-text{right:30px;top:78px;text-align:right;color:var(--white);width:330px}
.hero-text h2{font-size:20px;font-weight:700;line-height:34px}
.hero-text p{font-size:8.6px;font-weight:700;line-height:11px;margin-top:12px}
.hero-text .join{display:block;margin-top:16px;font-size:13px;font-weight:700}
.hero-dots{left:22px;top:200px;display:flex;gap:8px}
.hero-dots span{width:30px;height:30px;border-radius:50%;background:var(--blue-light);opacity:.6}
.hero-dots span:nth-child(n+3){background:#cfd8e2;opacity:1}

/* price finder */
.price-finder{left:711px;top:183px;width:257px;height:253px;border-radius:8px;background:var(--grey-bg);overflow:hidden}
.panel-title{height:36px;background:linear-gradient(90deg,var(--navy),var(--blue-light));color:var(--white);font-size:20px;font-weight:700;text-align:center;line-height:36px}
.price-input{left:24px;top:115px;width:220px;height:28px;background:var(--white);border:1px solid #ccc;font-size:11px;color:#888;padding:7px 12px}
.price-knob{left:14px;top:114px;width:30px;height:30px;border-radius:50%;background:radial-gradient(circle at 40% 40%,var(--blue-light),var(--navy))}
.hero-notch{left:684px;top:290px;width:22px;height:44px;border-radius:0 22px 22px 0;background:var(--navy)}

/* tabs */
.tabs{left:26px;top:446px;width:663px;height:33px;background:linear-gradient(var(--blue-light),var(--blue));display:flex;align-items:center;color:var(--white);font-size:15px;font-weight:700}
.tabs span{position:absolute}
.tab-knob{left:328px;top:479px;width:54px;height:26px;border-radius:0 0 27px 27px;background:var(--sky)}
.list-col{top:503px;height:322px;border:1px solid var(--grey-line);padding:8px 10px;font-size:10.5px;line-height:12px}
.list-col li{list-style:none;margin-bottom:15px}
.list-col b{display:block}
.rating{display:grid;grid-template-columns:1fr 1fr;gap:1px 10px;font-size:11px}
.rating li{margin:0;display:flex;align-items:center;gap:5px;height:15px}
.flag{width:16px;height:10px;display:inline-block}
.tray{left:26px;top:829px;width:676px;height:64px;border:1px solid var(--grey-line);border-top:none;border-radius:0 0 30px 30px;box-shadow:0 4px 6px rgba(0,0,0,.12)}
.tray-notch{left:325px;top:866px;width:52px;height:28px;border-radius:26px 26px 0 0;border:1px solid var(--grey-line);border-bottom:none;background:var(--white)}

/* ad */
.ad-slot{left:26px;top:905px;width:679px;height:86px;border:1px solid var(--grey-line);font-size:48px;font-weight:700;color:#bbb;padding:18px 14px}

/* news */
.news{left:711px;top:446px;width:257px;height:545px;border-radius:8px;border:1px solid var(--grey-line);overflow:hidden}
.news .panel-title{height:36px}
.news-knob{left:97px;top:36px;width:60px;height:20px;border-radius:0 0 30px 30px;background:var(--blue-deep)}
.news-body{left:18px;top:62px;width:225px;color:#333}
.news-body h3{font-size:17px;line-height:16px;font-weight:700;color:#444}
.news-body h4{font-size:14px;font-weight:700;margin:15px 0 7px;color:#333}
.news-body p{font-size:11px;line-height:12px}

/* footer */
.footer-bar{left:26px;top:1001px;width:942px;height:29px;background:linear-gradient(90deg,#a8a8a8,#f2f2f2)}
.site-footer{left:26px;top:1041px;width:942px;height:149px;border-radius:6px;background:linear-gradient(90deg,var(--navy),var(--blue-deep) 60%,var(--blue-light));color:var(--white);font-size:11px}
.footer-links{left:14px;top:14px}
.footer-links h4{font-size:11px;font-weight:400;margin-bottom:6px}
.footer-links ul{display:grid;grid-template-columns:repeat(4,171px);gap:3px 0;list-style:none}
.social{right:10px;top:10px;display:flex;gap:6px}
.social span{width:18px;height:18px;border-radius:3px;background:#c6d6ea}
.copyright{left:16px;top:120px;display:flex;align-items:center;gap:6px}
.copyright i{font-style:normal;width:14px;height:14px;border:1.5px solid #fff;border-radius:50%;font-size:9px;text-align:center;line-height:11px}
.legal{right:12px;top:125px;display:flex;gap:14px}
</style>
</head>
<body>

<header class="site-header abs">
  <div class="brand-band abs"></div>
  <div class="brand abs"><span class="brand-dot"></span>TradeoCup</div>
  <div class="lang abs"><span class="lang-flag"></span><span class="lang-select">English</span></div>
  <div class="countdown-box abs">
    <div class="countdown abs"><h3>Countdown</h3><div class="timer">18<small>d</small> 5<small>h</small> 16<small>m</small> 39<small>s</small></div></div>
    <div class="participants abs"><h3>ROUND<br>PARTISIPANTS</h3><b>456</b></div>
    <div class="box-links abs"><span style="left:26px">Check shedule ▸</span><span style="left:136px">Register</span><span style="left:212px">Login</span></div>
  </div>
</header>

<nav class="main-nav abs">
  <a href="#">About</a><a href="#">News</a><a href="#">Standings</a><a href="#">Schedule</a><a href="#">FAQ</a><a href="#">Brokers</a><a href="#">Download</a>
</nav>

<section class="hero abs">
  <div class="hero-art abs" role="img" aria-label="Glowing blue globe with world map"></div>
  <div class="hero-text abs">
    <h2>Find out more ...<br>Stay local, play global!</h2>
    <p>TradeoCup™ is an international trading competition to see who can make the most profit in two weeks with all players getting an equal starting sum. Participation is free with no strings attached and the prize money is real, with a total prize pool of $50,000!</p>
    <span class="join">Join Now</span>
  </div>
  <div class="hero-dots abs"><span></span><span></span><span></span><span></span></div>
</section>
<div class="hero-notch abs"></div>

<aside class="price-finder abs">
  <div class="panel-title">Price Finder</div>
  <div class="price-input abs" style="padding-left:24px">Enter Your Price</div>
  <div class="price-knob abs"></div>
</aside>

<div class="tabs abs">
  <span style="left:16px">Current Tournaments</span>
  <span style="left:247px">Ended Tournaments</span>
  <span style="left:504px">Players Rating</span>
</div>
<div class="tab-knob abs"></div>

<ul class="list-col abs" style="left:29px;width:204px">
  <li>28.08.11<b>Quisque vitae pede.</b>Nam et augue. Quisque vitae pede.</li>
  <li>29.08.11<b>Quisque vitae pede.</b>Nam et augue. Quisque vitae pede.</li>
  <li>30.08.11<b>Quisque vitae pede.</b>Nam et augue. Quisque vitae pede.</li>
  <li>01.09.11<b>Quisque vitae pede.</b>Nam et augue. Quisque vitae pede.</li>
  <li>02.09.11<b>Quisque vitae pede.</b>Nam et augue. Quisque vitae pede.</li>
  <li>02.09.11<b>Quisque vitae pede.</b>Nam et augue. Quisque vitae pede.</li>
</ul>
<ul class="list-col abs" style="left:262px;width:214px">
  <li>28.08.11<b>Quisque vitae pede.</b>Nam et augue. Quisque vitae pede.</li>
  <li>29.08.11<b>Quisque vitae pede.</b>Nam et augue. Quisque vitae pede.</li>
  <li>30.08.11<b>Quisque vitae pede.</b>Nam et augue. Quisque vitae pede.</li>
  <li>01.09.11<b>Quisque vitae pede.</b>Nam et augue. Quisque vitae pede.</li>
  <li>02.09.11<b>Quisque vitae pede.</b>Nam et augue. Quisque vitae pede.</li>
  <li>02.09.11<b>Quisque vitae pede.</b>Nam et augue. Quisque vitae pede.</li>
</ul>
<div class="list-col abs" style="left:512px;width:176px;padding:10px 14px">
  <ul class="rating">
    <li><span class="flag" style="background:linear-gradient(#fff 33%,#2a4aa0 33% 66%,#d22 66%)"></span>4812</li>
    <li><span class="flag" style="background:linear-gradient(90deg,#2a4aa0 33%,#f3d21e 33% 66%,#d22 66%)"></span>216</li>
    <li><span class="flag" style="background:linear-gradient(#fff 50%,#d22 50%)"></span>3257</li>
    <li><span class="flag" style="background:linear-gradient(#c22 25%,#f3c21e 25% 75%,#c22 75%)"></span>206</li>
    <li><span class="flag" style="background:linear-gradient(90deg,#2a4aa0 33%,#f3d21e 33% 66%,#d22 66%)"></span>3257</li>
    <li><span class="flag" style="background:linear-gradient(#fff 50%,#d22 50%)"></span>167</li>
    <li><span class="flag" style="background:#d22"></span>2408</li>
    <li><span class="flag" style="background:linear-gradient(#d22 33%,#fff 33% 66%,#2a4aa0 66%)"></span>162</li>
    <li><span class="flag" style="background:linear-gradient(#000 33%,#d22 33% 66%,#f3c21e 66%)"></span>2115</li>
    <li><span class="flag" style="background:#2a9a3a"></span>128</li>
    <li><span class="flag" style="background:linear-gradient(#3a7ad0 50%,#f3d21e 50%)"></span>1797</li>
    <li><span class="flag" style="background:linear-gradient(#fff 50%,#d22 50%)"></span>97</li>
    <li><span class="flag" style="background:linear-gradient(#fff 33%,#2a4aa0 33% 66%,#d22 66%)"></span>1705</li>
    <li><span class="flag" style="background:linear-gradient(90deg,#2a9a3a 33%,#fff 33% 66%,#2a9a3a 66%)"></span>83</li>
    <li><span class="flag" style="background:linear-gradient(#a22 40%,#fff 40% 60%,#a22 60%)"></span>1689</li>
    <li><span class="flag" style="background:linear-gradient(#c8202f 0 100%)"></span>83</li>
    <li><span class="flag" style="background:linear-gradient(#f3c21e 33%,#2a9a3a 33% 66%,#d22 66%)"></span>1623</li>
    <li><span class="flag" style="background:linear-gradient(90deg,#2a9a3a 33%,#fff 33% 66%,#d22 66%)"></span>82</li>
    <li><span class="flag" style="background:linear-gradient(#f3c21e 33%,#2a9a3a 33% 66%,#d22 66%)"></span>1530</li><li></li>
    <li><span class="flag" style="background:linear-gradient(#d22 50%,#fff 50%)"></span>1509</li><li></li>
    <li><span class="flag" style="background:linear-gradient(#d22 33%,#fff 33% 66%,#2a9a3a 66%)"></span>886</li><li></li>
    <li><span class="flag" style="background:#d22"></span>783</li><li></li>
    <li><span class="flag" style="background:linear-gradient(#d22 20%,#fff 20% 40%,#d22 40% 60%,#fff 60% 80%,#d22 80%)"></span>775</li><li></li>
    <li><span class="flag" style="background:linear-gradient(#d22 50%,#fff 50%)"></span>680</li><li></li>
    <li><span class="flag" style="background:#d22"></span>373</li><li></li>
    <li><span class="flag" style="background:#5bc0de"></span>373</li><li></li>
    <li><span class="flag" style="background:linear-gradient(#f39a1e 33%,#fff 33% 66%,#2a9a3a 66%)"></span>323</li><li></li>
  </ul>
</div>
<div class="tray abs"></div>
<div class="tray-notch abs"></div>

<div class="ad-slot abs">ADV</div>

<aside class="news abs">
  <div class="panel-title">Latest News</div>
  <div class="news-knob abs"></div>
  <div class="news-body abs">
    <h3>EVENTS<br><span style="font-size:15px">we are involved in<br>start in:</span></h3>
    <h4>Quisque vitae pede.</h4>
    <p>Quisque vitae pede. Nam et augue. Sed a elit. Ut vel massa. Suspendisse nibh pede, ultrices vitae,ultrices nec, mollis non nibh.Quisque vitae pede. Nam et augue.</p>
    <h4>Quisque vitae pede.</h4>
    <p>Quisque vitae pede. Nam et augue. Sed a elit. Ut vel massa. Suspendisse nibh pede, ultrices vitae,ultrices nec, mollis non nibh.Quisque vitae pede. Nam et augue.</p>
    <h4>Quisque vitae pede.</h4>
    <p>Quisque vitae pede. Nam et augue. Sed a elit. Ut vel massa. Suspendisse nibh pede, ultrices vitae,ultrices nec, mollis non nibh.Quisque vitae pede. Nam et augue.</p>
    <h4>Quisque vitae pede.</h4>
    <p>Quisque vitae pede. Nam et augue. Sed a elit. Ut vel massa. Suspendisse nibh pede, ultrices vitae,ultrices nec, mollis non nibh.Quisque vitae pede. Nam et augue.</p>
  </div>
</aside>

<div class="footer-bar abs"></div>
<footer class="site-footer abs">
  <div class="footer-links abs">
    <h4>SOME LINKS</h4>
    <ul>
      <li>Quisque vitae pede.</li><li>Quisque vitae pede.</li><li>Quisque vitae pede.</li><li>Quisque vitae pede.</li>
      <li>Quisque vitae pede.</li><li>Quisque vitae pede.</li><li>Quisque vitae pede.</li><li>Quisque vitae pede.</li>
      <li>Quisque vitae pede.</li><li>Quisque vitae pede.</li><li>Quisque vitae pede.</li><li>Quisque vitae pede.</li>
      <li>Quisque vitae pede.</li><li>Quisque vitae pede.</li><li>Quisque vitae pede.</li><li>Quisque vitae pede.</li>
    </ul>
  </div>
  <div class="social abs"><span></span><span></span><span></span><span></span>
    <svg width="24" height="18" viewBox="0 0 24 18" aria-label="Email"><rect x="1" y="1" width="22" height="16" fill="none" stroke="#fff" stroke-width="1.5"/><path d="M1 1l11 9 11-9" fill="none" stroke="#fff" stroke-width="1.5"/></svg>
  </div>
  <div class="copyright abs">2011 <i>C</i> Copyrigtht . All rights reserved.</div>
  <div class="legal abs"><span>Live Chat</span><span>Terms&amp;Conditions</span><span>Contact Us</span></div>
</footer>

</body>
</html>
```